The Brightwater Compass Business Card

We need an attractive business card with the logo that we bought from ArtVantly last year.
Our mission is to contribute to change the way today's leaders manage business companies bringing value to the workplace and helping them to build a new model of creating wealth.
Our logo is clear about our values : we seek Positive Change through People and are convinced that the pursuit of individual well-being and the chase of economic results can converge with the right management.
Management Consulting
Corinne Fabrelle
+34 612 98 70 31
corinne.fabrelle@thebrightwatercompass-mail.net
www.thebrightwatercompass-mail.net

```html
<!DOCTYPE html>
<html lang="en">
<head>
<meta charset="utf-8">
<title>The Brightwater Compass – Business Card</title>
<link href="https://fonts.googleapis.com/css2?family=Roboto:wght@400;500;700&display=swap" rel="stylesheet">
<style>
  :root {
    --teal: #14807c;
    --ink: #262b4a;
    --paper: #ffffff;
    --backdrop: #6b7478;
  }
  * { box-sizing: border-box; margin: 0; padding: 0; }
  html, body { width: 1200px; height: 900px; overflow: hidden; }
  body {
    background: var(--backdrop);
    font-family: "Roboto", Arial, sans-serif;
    display: flex;
    flex-direction: column;
    align-items: center;
    justify-content: center;
    gap: 44px;
  }
  .card {
    position: relative;
    width: 600px;
    height: 343px;
    background: var(--paper);
    box-shadow: 0 6px 18px rgba(0,0,0,0.25);
    overflow: hidden;
  }
  /* front */
  .card-front .edge-tab {
    position: absolute;
    width: 10px;
    height: 100px;
    background: var(--teal);
  }
  .card-front .edge-tab--left { left: 0; top: 60px; border-radius: 0 6px 6px 0; }
  .card-front .edge-tab--right { right: 0; top: 200px; border-radius: 6px 0 0 6px; }
  .brand {
    position: absolute;
    left: 0; right: 0; top: 120px;
    display: flex;
    align-items: center;
    justify-content: center;
    gap: 14px;
    color: var(--teal);
    font-weight: 500;
  }
  .brand-mark {
    width: 46px; height: 46px;
    border-radius: 50%;
    background: var(--teal);
  }
  .brand-name { font-size: 30px; letter-spacing: 0.5px; }
  .front-url {
    position: absolute;
    left: 56px; bottom: 40px;
    font-size: 15px;
    color: var(--ink);
  }
  /* back */
  .card-back .brand {
    top: 38px; left: 54px; right: auto;
    justify-content: flex-start;
    gap: 10px;
  }
  .card-back .brand-mark { width: 30px; height: 30px; }
  .card-back .brand-name { font-size: 20px; }
  .person {
    position: absolute;
    left: 54px; top: 110px;
  }
  .person-name {
    font-size: 22px;
    font-weight: 700;
    color: var(--teal);
  }
  .person-role {
    font-size: 12px;
    color: var(--ink);
    text-transform: uppercase;
    margin-top: 2px;
  }
  .rule {
    position: absolute;
    left: 54px; top: 170px;
    width: 470px; height: 2px;
    background: var(--teal);
  }
  .contacts {
    position: absolute;
    left: 54px; top: 188px;
    list-style: none;
    font-size: 13px;
    color: var(--ink);
    line-height: 22px;
  }
  .contacts li { display: flex; align-items: center; gap: 8px; }
  .contacts svg { width: 12px; height: 12px; fill: var(--teal); flex: none; }
</style>
</head>
<body>
  <section class="card card-front">
    <span class="edge-tab edge-tab--left"></span>
    <span class="edge-tab edge-tab--right"></span>
    <div class="brand">
      <span class="brand-mark"></span>
      <span class="brand-name">The Brightwater Compass</span>
    </div>
    <p class="front-url">www.thebrightwatercompass-mail.net</p>
  </section>

  <section class="card card-back">
    <div class="brand">
      <span class="brand-mark"></span>
      <span class="brand-name">The Brightwater Compass</span>
    </div>
    <div class="person">
      <p class="person-name">Corinne Fabrelle</p>
      <p class="person-role">Founder</p>
    </div>
    <span class="rule"></span>
    <ul class="contacts">
      <li>
        <svg viewBox="0 0 24 24" aria-hidden="true"><path d="M6.6 10.8a15 15 0 0 0 6.6 6.6l2.2-2.2c.3-.3.7-.4 1-.2 1.1.4 2.3.6 3.6.6.6 0 1 .4 1 1V20c0 .6-.4 1-1 1A17 17 0 0 1 3 4c0-.6.4-1 1-1h3.5c.6 0 1 .4 1 1 0 1.3.2 2.5.6 3.6.1.3 0 .7-.2 1z"/></svg>
        +34 612 98 70 31
      </li>
      <li>
        <svg viewBox="0 0 24 24" aria-hidden="true"><path d="M12 2a10 10 0 1 0 0 20 10 10 0 0 0 0-20zm0 2c1 0 2.3 1.8 2.9 5H9.1C9.7 5.8 11 4 12 4zM4.3 14a8 8 0 0 1 0-4h2.9a17 17 0 0 0 0 4zm4.8 1h5.8c-.6 3.2-1.9 5-2.9 5s-2.3-1.8-2.9-5zm0-1a15 15 0 0 1 0-4h5.8a15 15 0 0 1 0 4zm7.7 0a17 17 0 0 0 0-4h2.9a8 8 0 0 1 0 4z"/></svg>
        www.thebrightwatercompass-mail.net
      </li>
      <li>
        <svg viewBox="0 0 24 24" aria-hidden="true"><path d="M2 5h20v14H2zm2 2v.5l8 5 8-5V7z"/></svg>
        corinne.fabrelle@thebrightwatercompass-mail.net
      </li>
    </ul>
  </section>
</body>
</html>
```